Vantor Clip Design Project

Two sided Flyer for vantor clip
see: www.vantor-clip.example
I have attached a copy with dimensions of last year's winner.
Replace Teodor Wallisch with Marcus Fenby

Use contact data from following web page link:
https://www.harlowbrisk.example/cgi/getHTML.cgi?page=/en_CA/fa/index.html&CIRN=418302

see uploaded photo file

Reason: Need more designs so am upgrading to guaranteed payout. i'll be submitting a colour picture of me soon.

fee is now guiaranteed with 15 day extension

```html
<!DOCTYPE html>
<html lang="en">
<head>
<meta charset="utf-8">
<title>2013 Pen Calendar – Harlow Brisk</title>
<link rel="stylesheet" href="https://fonts.googleapis.com/css2?family=Arimo:wght@400;700&family=Roboto+Condensed:wght@700&display=swap">
<style>
  :root {
    --green: #17663f;
    --yellow: #f4b428;
    --ink: #111111;
    --white: #ffffff;
  }
  * { box-sizing: border-box; margin: 0; padding: 0; }
  html, body { width: 1200px; height: 438px; overflow: hidden; background: var(--green); }
  .card {
    position: relative; width: 1200px; height: 438px;
    background: var(--green); color: var(--white);
    font-family: "Arimo", Arial, sans-serif;
  }
  .year {
    position: absolute; left: 16px; top: 4px;
    font-size: 36px; font-weight: 400; line-height: 40px;
  }
  .months {
    position: absolute; left: 16px; top: 44px;
    display: grid; grid-template-columns: repeat(6, 148px);
    grid-template-rows: repeat(2, 172px);
    column-gap: 5px; row-gap: 6px;
  }
  .month { display: flex; flex-direction: column; }
  .month-name {
    height: 20px; font-size: 15px; line-height: 18px; padding-left: 3px; color: var(--white);
  }
  .sheet { flex: 1; background: var(--yellow); padding: 2px 2px 0; }
  .weekdays, .days {
    display: grid; grid-template-columns: repeat(7, 1fr); list-style: none; text-align: center;
  }
  .weekdays li { font-size: 7px; font-weight: 700; color: var(--ink); line-height: 12px; }
  .days li {
    font-family: "Roboto Condensed", "Arial Narrow", sans-serif;
    font-weight: 700; font-size: 17px; line-height: 23px; color: var(--ink);
  }
  .s1 { grid-column-start: 2; } .s2 { grid-column-start: 3; } .s3 { grid-column-start: 4; }
  .s4 { grid-column-start: 5; } .s5 { grid-column-start: 6; } .s6 { grid-column-start: 7; }
  .brand {
    position: absolute; left: 938px; top: 44px; width: 92px; height: 348px;
    display: flex; align-items: center; justify-content: center;
  }
  .brand-name {
    writing-mode: vertical-rl; transform: rotate(180deg);
    font-weight: 700; font-size: 50px; letter-spacing: 1px; color: var(--white); white-space: nowrap;
  }
  .brand-tag {
    position: absolute; left: 1030px; top: 44px; height: 348px;
    writing-mode: vertical-rl; transform: rotate(180deg);
    font-size: 16px; font-weight: 700; text-transform: uppercase; color: var(--white);
    display: flex; align-items: center;
  }
  .note {
    position: absolute; left: 16px; right: 10px; top: 396px;
    font-size: 19.5px; line-height: 20px; color: var(--white);
  }
</style>
</head>
<body>
<div class="card">
  <div class="year">2013</div>

  <div class="months">
    <section class="month"><h2 class="month-name">January</h2><div class="sheet">
      <ul class="weekdays"><li>SUN</li><li>MON</li><li>TUE</li><li>WED</li><li>THU</li><li>FRI</li><li>SAT</li></ul>
      <ol class="days"><li class="s2">1</li><li>2</li><li>3</li><li>4</li><li>5</li><li>6</li><li>7</li><li>8</li><li>9</li><li>10</li><li>11</li><li>12</li><li>13</li><li>14</li><li>15</li><li>16</li><li>17</li><li>18</li><li>19</li><li>20</li><li>21</li><li>22</li><li>23</li><li>24</li><li>25</li><li>26</li><li>27</li><li>28</li><li>29</li><li>30</li><li>31</li></ol>
    </div></section>

    <section class="month"><h2 class="month-name">February</h2><div class="sheet">
      <ul class="weekdays"><li>SUN</li><li>MON</li><li>TUE</li><li>WED</li><li>THU</li><li>FRI</li><li>SAT</li></ul>
      <ol class="days"><li class="s5">1</li><li>2</li><li>3</li><li>4</li><li>5</li><li>6</li><li>7</li><li>8</li><li>9</li><li>10</li><li>11</li><li>12</li><li>13</li><li>14</li><li>15</li><li>16</li><li>17</li><li>18</li><li>19</li><li>20</li><li>21</li><li>22</li><li>23</li><li>24</li><li>25</li><li>26</li><li>27</li><li>28</li></ol>
    </div></section>

    <section class="month"><h2 class="month-name">March</h2><div class="sheet">
      <ul class="weekdays"><li>SUN</li><li>MON</li><li>TUE</li><li>WED</li><li>THU</li><li>FRI</li><li>SAT</li></ul>
      <ol class="days"><li class="s5">1</li><li>2</li><li>3</li><li>4</li><li>5</li><li>6</li><li>7</li><li>8</li><li>9</li><li>10</li><li>11</li><li>12</li><li>13</li><li>14</li><li>15</li><li>16</li><li>17</li><li>18</li><li>19</li><li>20</li><li>21</li><li>22</li><li>23</li><li>24</li><li>25</li><li>26</li><li>27</li><li>28</li><li>29</li><li>30</li><li>31</li></ol>
    </div></section>

    <section class="month"><h2 class="month-name">April</h2><div class="sheet">
      <ul class="weekdays"><li>SUN</li><li>MON</li><li>TUE</li><li>WED</li><li>THU</li><li>FRI</li><li>SAT</li></ul>
      <ol class="days"><li class="s1">1</li><li>2</li><li>3</li><li>4</li><li>5</li><li>6</li><li>7</li><li>8</li><li>9</li><li>10</li><li>11</li><li>12</li><li>13</li><li>14</li><li>15</li><li>16</li><li>17</li><li>18</li><li>19</li><li>20</li><li>21</li><li>22</li><li>23</li><li>24</li><li>25</li><li>26</li><li>27</li><li>28</li><li>29</li><li>30</li></ol>
    </div></section>

    <section class="month"><h2 class="month-name">May</h2><div class="sheet">
      <ul class="weekdays"><li>SUN</li><li>MON</li><li>TUE</li><li>WED</li><li>THU</li><li>FRI</li><li>SAT</li></ul>
      <ol class="days"><li class="s3">1</li><li>2</li><li>3</li><li>4</li><li>5</li><li>6</li><li>7</li><li>8</li><li>9</li><li>10</li><li>11</li><li>12</li><li>13</li><li>14</li><li>15</li><li>16</li><li>17</li><li>18</li><li>19</li><li>20</li><li>21</li><li>22</li><li>23</li><li>24</li><li>25</li><li>26</li><li>27</li><li>28</li><li>29</li><li>30</li><li>31</li></ol>
    </div></section>

    <section class="month"><h2 class="month-name">June</h2><div class="sheet">
      <ul class="weekdays"><li>SUN</li><li>MON</li><li>TUE</li><li>WED</li><li>THU</li><li>FRI</li><li>SAT</li></ul>
      <ol class="days"><li class="s6">1</li><li>2</li><li>3</li><li>4</li><li>5</li><li>6</li><li>7</li><li>8</li><li>9</li><li>10</li><li>11</li><li>12</li><li>13</li><li>14</li><li>15</li><li>16</li><li>17</li><li>18</li><li>19</li><li>20</li><li>21</li><li>22</li><li>23</li><li>24</li><li>25</li><li>26</li><li>27</li><li>28</li><li>29</li><li>30</li></ol>
    </div></section>

    <section class="month"><h2 class="month-name">July</h2><div class="sheet">
      <ul class="weekdays"><li>SUN</li><li>MON</li><li>TUE</li><li>WED</li><li>THU</li><li>FRI</li><li>SAT</li></ul>
      <ol class="days"><li class="s1">1</li><li>2</li><li>3</li><li>4</li><li>5</li><li>6</li><li>7</li><li>8</li><li>9</li><li>10</li><li>11</li><li>12</li><li>13</li><li>14</li><li>15</li><li>16</li><li>17</li><li>18</li><li>19</li><li>20</li><li>21</li><li>22</li><li>23</li><li>24</li><li>25</li><li>26</li><li>27</li><li>28</li><li>29</li><li>30</li><li>31</li></ol>
    </div></section>

    <section class="month"><h2 class="month-name">August</h2><div class="sheet">
      <ul class="weekdays"><li>SUN</li><li>MON</li><li>TUE</li><li>WED</li><li>THU</li><li>FRI</li><li>SAT</li></ul>
      <ol class="days"><li class="s4">1</li><li>2</li><li>3</li><li>4</li><li>5</li><li>6</li><li>7</li><li>8</li><li>9</li><li>10</li><li>11</li><li>12</li><li>13</li><li>14</li><li>15</li><li>16</li><li>17</li><li>18</li><li>19</li><li>20</li><li>21</li><li>22</li><li>23</li><li>24</li><li>25</li><li>26</li><li>27</li><li>28</li><li>29</li><li>30</li><li>31</li></ol>
    </div></section>

    <section class="month"><h2 class="month-name">September</h2><div class="sheet">
      <ul class="weekdays"><li>SUN</li><li>MON</li><li>TUE</li><li>WED</li><li>THU</li><li>FRI</li><li>SAT</li></ul>
      <ol class="days"><li>1</li><li>2</li><li>3</li><li>4</li><li>5</li><li>6</li><li>7</li><li>8</li><li>9</li><li>10</li><li>11</li><li>12</li><li>13</li><li>14</li><li>15</li><li>16</li><li>17</li><li>18</li><li>19</li><li>20</li><li>21</li><li>22</li><li>23</li><li>24</li><li>25</li><li>26</li><li>27</li><li>28</li><li>29</li><li>30</li></ol>
    </div></section>

    <section class="month"><h2 class="month-name">October</h2><div class="sheet">
      <ul class="weekdays"><li>SUN</li><li>MON</li><li>TUE</li><li>WED</li><li>THU</li><li>FRI</li><li>SAT</li></ul>
      <ol class="days"><li class="s2">1</li><li>2</li><li>3</li><li>4</li><li>5</li><li>6</li><li>7</li><li>8</li><li>9</li><li>10</li><li>11</li><li>12</li><li>13</li><li>14</li><li>15</li><li>16</li><li>17</li><li>18</li><li>19</li><li>20</li><li>21</li><li>22</li><li>23</li><li>24</li><li>25</li><li>26</li><li>27</li><li>28</li><li>29</li><li>30</li><li>31</li></ol>
    </div></section>

    <section class="month"><h2 class="month-name">November</h2><div class="sheet">
      <ul class="weekdays"><li>SUN</li><li>MON</li><li>TUE</li><li>WED</li><li>THU</li><li>FRI</li><li>SAT</li></ul>
      <ol class="days"><li class="s5">1</li><li>2</li><li>3</li><li>4</li><li>5</li><li>6</li><li>7</li><li>8</li><li>9</li><li>10</li><li>11</li><li>12</li><li>13</li><li>14</li><li>15</li><li>16</li><li>17</li><li>18</li><li>19</li><li>20</li><li>21</li><li>22</li><li>23</li><li>24</li><li>25</li><li>26</li><li>27</li><li>28</li><li>29</li><li>30</li></ol>
    </div></section>

    <section class="month"><h2 class="month-name">December</h2><div class="sheet">
      <ul class="weekdays"><li>SUN</li><li>MON</li><li>TUE</li><li>WED</li><li>THU</li><li>FRI</li><li>SAT</li></ul>
      <ol class="days"><li>1</li><li>2</li><li>3</li><li>4</li><li>5</li><li>6</li><li>7</li><li>8</li><li>9</li><li>10</li><li>11</li><li>12</li><li>13</li><li>14</li><li>15</li><li>16</li><li>17</li><li>18</li><li>19</li><li>20</li><li>21</li><li>22</li><li>23</li><li>24</li><li>25</li><li>26</li><li>27</li><li>28</li><li>29</li><li>30</li><li>31</li></ol>
    </div></section>
  </div>

  <div class="brand"><span class="brand-name">Harlow Brisk</span></div>
  <div class="brand-tag">Steady Planning Ahead</div>

  <p class="note">Eventually, this calendar will expire or the ink will run dry... when that happens, return this pen to Marcus and received a new one. All the best for a great year.</p>
</div>
</body>
</html>
```